2013 Global Campus Assembly

The Global Campus Assembly is searching for a poster design that can also serve as cover art for its conference program (8.5x11). The event is entering its sixth year and will be held in Vancouver, Canada. It is modeled after the Planetary Trade Summit, and meets yearly to discuss the University, how it is formed, and its place in an ever changing society.

Many perspectives are shared as the conference attracts people from all over the world. This past year's meeting had almost 30 countries represented.

Issues and discussions include loss of funding, especially in times of economic turmoil, the necessity of college degrees, electronic education, the place of the University in the world, etc.

The theme for 2013 will revolve around Higher Education and the Future of Democracy.

We would like something bold and indicative of the ideas to be discussed, but not controversial. No current color preferences. Ideas that pertain to democracy and/or Vancouver are welcome.

Target Market(s)

Scholars, Teachers, Administrators, Students, Provosts, Deans, Distance Educators

Industry/Entity Type

Electronic

Requirements
Must have
• Please include text:
Sixth Global Campus Assembly
10-11 January 2013
NKT-Ferrow Plaza
Vancouver, Canada

```html
<!DOCTYPE html>
<html lang="en">
<head>
<meta charset="utf-8">
<title>Sixth Global Campus Assembly</title>
<link rel="stylesheet" href="https://fonts.googleapis.com/css2?family=PT+Sans:wght@400;700&display=swap">
<style>
  :root {
    --blush: #fff2f7;
    --rose: #ff9cc2;
    --pink: #fc5d99;
    --magenta: #fa1c74;
    --region-top: rgba(234, 204, 232, 0.92);
    --region-bottom: rgba(228, 100, 172, 0.6);
    --shore-band: rgba(168, 84, 122, 0.38);
    --shore-line: rgba(90, 60, 80, 0.55);
    --text: #ffffff;
    --glow: rgba(255, 255, 255, 0.6);
  }
  html, body {
    margin: 0;
    padding: 0;
    overflow: hidden;
    background: #ffffff;
  }
  .poster {
    position: relative;
    width: 932px;
    height: 1200px;
    overflow: hidden;
    background: linear-gradient(180deg, var(--blush) 0%, var(--rose) 28%, var(--pink) 62%, var(--magenta) 100%);
    font-family: "PT Sans", "Myriad Pro", sans-serif;
    color: var(--text);
  }
  .city-map {
    position: absolute;
    inset: 0;
  }
  .city-map__area {
    position: absolute;
    background: linear-gradient(180deg, var(--region-top) 0%, var(--region-bottom) 100%);
    border: 22px solid var(--shore-band);
    outline: 1px solid var(--shore-line);
    outline-offset: -12px;
  }
  .city-map__area--north {
    left: 300px;
    top: 90px;
    width: 210px;
    height: 300px;
    border-bottom: none;
    border-radius: 90px 110px 0 0;
    background: linear-gradient(180deg, rgba(236, 212, 236, 0.92) 0%, var(--region-top) 100%);
  }
  .city-map__area--main {
    left: -22px;
    top: 260px;
    width: 932px;
    height: 600px;
    border-right: none;
    border-radius: 140px 0 40px 260px;
    background: linear-gradient(180deg, var(--region-top) 0%, var(--region-bottom) 100%);
  }
  .title {
    position: absolute;
    right: 30px;
    top: 372px;
    margin: 0;
    text-align: right;
    font-weight: 400;
    font-size: 84px;
    line-height: 97px;
    letter-spacing: -0.5px;
    text-shadow: 0 0 12px var(--glow);
  }
  .title span { display: block; }
  .details {
    position: absolute;
    left: 0;
    right: 0;
    bottom: 28px;
    margin: 0;
    text-align: center;
    font-size: 33px;
    font-weight: 700;
    letter-spacing: -0.4px;
    white-space: nowrap;
  }
</style>
</head>
<body>
  <main class="poster">
    <div class="city-map" role="img" aria-label="Map of Vancouver's shoreline and downtown peninsula">
      <div class="city-map__area city-map__area--main"></div>
      <div class="city-map__area city-map__area--north"></div>
    </div>
    <h1 class="title">
      <span>Sixth</span>
      <span>Global</span>
      <span>Campus</span>
      <span>Assembly</span>
    </h1>
    <p class="details">10-11 January 2013. NKT-Ferrow Plaza. Vancouver, Canada</p>
  </main>
</body>
</html>
```